Menu redesign of existing iPhone app Lumora

We need a design upgrade for a footer menu of an iPhone app. We need to incorporate a new button for competitions/missions and it should be extremely modern and clean. The central button to create a Lumora cannot be too different as our current users are familiar with its usage.

I have attached screenshots of the curent newsfeed and menu.

Target Market(s)

Photography lovers/ design lovers

Font styles to use
Sans Serif

Requirements
Must have
• Lumora Button,
• Home button,
• My Profile button,
• Find friends button,
• Notifications button,
• Settings button,
• Missions/Competition Button
Nice to have
• Similar Lumora button as existing on the app

```html
<!DOCTYPE html>
<html lang="en">
<head>
<meta charset="utf-8">
<title>Lumora – Footer Menu Redesign</title>
<link href="https://fonts.googleapis.com/css2?family=Nunito+Sans:wght@400;600&family=Inter:wght@400;500&display=swap" rel="stylesheet">
<style>
  :root {
    --canvas: #e2e2e2;
    --white: #ffffff;
    --ink: #2d2d2d;
    --ink-soft: #555555;
    --status-bg: #f4f4f4;
    --band-dim: rgba(170, 170, 170, 0.95);
    --dim: rgba(20, 30, 45, 0.32);
    --icon: #333333;
  }
  * { box-sizing: border-box; margin: 0; padding: 0; }
  html, body { width: 1200px; height: 963px; overflow: hidden; background: var(--canvas); }
  body { position: relative; font-family: "Nunito Sans", sans-serif; color: var(--ink); }

  .screen {
    position: absolute; top: 81px; width: 451px; height: 800px;
    overflow: hidden; background: #000;
  }
  .screen--menu-open { left: 99px; }
  .screen--menu-closed { left: 650px; }

  .status-bar {
    position: absolute; top: 0; left: 0; right: 0; height: 35px; z-index: 5;
    background: var(--status-bg); display: flex; align-items: center; justify-content: space-between;
    padding: 0 10px; font-family: "Inter", sans-serif; font-size: 15px; color: #111;
  }
  .status-bar__time { position: absolute; left: 0; right: 0; text-align: center; }
  .status-bar__left, .status-bar__right { display: flex; align-items: center; gap: 6px; }
  .battery { width: 34px; height: 13px; border: 1.5px solid #111; border-radius: 3px; padding: 1px; position: relative; }
  .battery::before { content: ""; display: block; width: 100%; height: 100%; background: #111; border-radius: 1px; }
  .battery::after { content: ""; position: absolute; right: -4px; top: 3px; width: 2px; height: 5px; background: #111; }

  .feed-photo {
    position: absolute; top: 35px; left: 0; right: 0; bottom: 0;
    background: linear-gradient(to bottom,
      #1f3a1e 0%, #3c5624 8%, #b79a2c 16%, #c8a93a 21%,
      #2f5f9e 24%, #3a6fb8 40%, #6f9ad4 60%, #a9c2de 66%,
      #4b6f8e 72%, #385a3c 84%, #3f6131 91%, #b7962f 97%, #c9a73a 100%);
  }
  .dim-layer { position: absolute; top: 35px; left: 0; right: 0; bottom: 0; background: var(--dim); }

  .post-band {
    position: absolute; top: 201px; left: 0; right: 0; height: 87px;
    background: var(--white); z-index: 3;
  }
  .screen--menu-open .post-band { background: var(--band-dim); }
  .post-band::after {
    content: ""; position: absolute; left: 211px; bottom: -14px;
    border-left: 14px solid transparent; border-right: 14px solid transparent;
    border-top: 14px solid var(--white);
  }
  .screen--menu-open .post-band::after { border-top-color: var(--band-dim); }

  .avatar {
    position: absolute; left: 42px; top: 15px; width: 56px; height: 56px; border-radius: 50%;
    background: radial-gradient(circle at 50% 40%, #c27a5a, #6b3a2a 70%, #3c5a3a);
    border: 2px solid rgba(255,255,255,0.7);
  }
  .post-title {
    position: absolute; left: 0; right: 0; top: 14px; text-align: center;
    font-size: 23px; font-weight: 400; letter-spacing: 1.2px; color: var(--ink);
  }
  .post-time {
    position: absolute; left: 0; right: 0; top: 48px; text-align: center;
    font-size: 14px; letter-spacing: 0.6px; color: var(--ink-soft);
  }
  .post-stats { position: absolute; left: 370px; top: 20px; font-size: 13px; color: var(--ink-soft); }
  .post-stats__row { display: flex; align-items: center; gap: 4px; height: 25px; }

  .action-sheet { position: absolute; left: 117px; top: 607px; width: 214px; z-index: 4; }
  .action-sheet__item {
    display: block; height: 37px; margin-bottom: 5px; background: var(--white);
    text-align: center; line-height: 37px; font-size: 16px; letter-spacing: 1px; color: var(--ink);
  }
  .action-sheet__item--cancel { margin-top: 17px; }

  .footer-menu { position: absolute; left: 0; top: 680px; width: 451px; height: 52px; z-index: 4; }
  .footer-menu__bar { position: absolute; top: 0; height: 52px; background: var(--white); }
  .footer-menu__bar--left { left: 10px; width: 176px; }
  .footer-menu__bar--right { left: 266px; width: 178px; }
  .footer-menu__icon { position: absolute; top: 12px; width: 28px; height: 28px; margin-left: -14px; }
  .capture-button { position: absolute; left: 181px; top: -19px; width: 90px; height: 90px; }
</style>
</head>
<body>

<!-- Screen with action sheet open -->
<section class="screen screen--menu-open">
  <div class="status-bar">
    <span class="status-bar__left">
      <svg width="48" height="8" viewBox="0 0 48 8"><g fill="#111"><circle cx="4" cy="4" r="3.6"/><circle cx="13" cy="4" r="3.6"/><circle cx="22" cy="4" r="3.6"/><circle cx="31" cy="4" r="3.6"/><circle cx="40" cy="4" r="3.6"/></g></svg>
      <svg width="16" height="12" viewBox="0 0 16 12"><g fill="none" stroke="#111" stroke-width="1.6"><path d="M1 4a10 10 0 0 1 14 0"/><path d="M4 7a6 6 0 0 1 8 0"/></g><circle cx="8" cy="10.5" r="1.5" fill="#111"/></svg>
    </span>
    <span class="status-bar__time">9:41 AM</span>
    <span class="status-bar__right">100% <span class="battery"></span></span>
  </div>
  <div class="feed-photo" role="img" aria-label="Landscape photo: golden meadow and forest under a blue sky with mountains"></div>
  <div class="dim-layer"></div>

  <div class="post-band">
    <div class="avatar" role="img" aria-label="Profile photo"></div>
    <div class="post-title">Vela Staff Pick</div>
    <div class="post-time">15 hours ago</div>
    <div class="post-stats">
      <div class="post-stats__row"><svg width="20" height="18" viewBox="0 0 20 18"><path d="M10 2c4.4 0 8 2.7 8 6s-3.6 6-8 6c-1 0-2-.1-2.8-.4L3 16l1.2-3.3C2.8 11.6 2 9.9 2 8c0-3.3 3.6-6 8-6z" fill="none" stroke="#555" stroke-width="1.2"/></svg>53</div>
      <div class="post-stats__row"><svg width="20" height="18" viewBox="0 0 20 18"><path d="M10 1l2.5 5.3 5.7.6-4.3 3.9 1.2 5.7L10 13.6 4.9 16.5l1.2-5.7L1.8 6.9l5.7-.6z" fill="none" stroke="#555" stroke-width="1.2"/></svg>122</div>
    </div>
  </div>

  <nav class="action-sheet">
    <span class="action-sheet__item">Create Video</span>
    <span class="action-sheet__item">Select Video</span>
    <span class="action-sheet__item">Select Lumora Pic</span>
    <span class="action-sheet__item action-sheet__item--cancel">Cancel</span>
  </nav>
</section>

<!-- Screen with new footer menu -->
<section class="screen screen--menu-closed">
  <div class="status-bar">
    <span class="status-bar__left">
      <svg width="48" height="8" viewBox="0 0 48 8"><g fill="#111"><circle cx="4" cy="4" r="3.6"/><circle cx="13" cy="4" r="3.6"/><circle cx="22" cy="4" r="3.6"/><circle cx="31" cy="4" r="3.6"/><circle cx="40" cy="4" r="3.6"/></g></svg>
      <svg width="16" height="12" viewBox="0 0 16 12"><g fill="none" stroke="#111" stroke-width="1.6"><path d="M1 4a10 10 0 0 1 14 0"/><path d="M4 7a6 6 0 0 1 8 0"/></g><circle cx="8" cy="10.5" r="1.5" fill="#111"/></svg>
    </span>
    <span class="status-bar__time">9:41 AM</span>
    <span class="status-bar__right">100% <span class="battery"></span></span>
  </div>
  <div class="feed-photo" role="img" aria-label="Landscape photo: golden meadow and forest under a blue sky with mountains"></div>

  <div class="post-band">
    <div class="avatar" role="img" aria-label="Profile photo"></div>
    <div class="post-title">Vela Staff Pick</div>
    <div class="post-time">15 hours ago</div>
    <div class="post-stats">
      <div class="post-stats__row"><svg width="20" height="18" viewBox="0 0 20 18"><path d="M10 2c4.4 0 8 2.7 8 6s-3.6 6-8 6c-1 0-2-.1-2.8-.4L3 16l1.2-3.3C2.8 11.6 2 9.9 2 8c0-3.3 3.6-6 8-6z" fill="none" stroke="#555" stroke-width="1.2"/></svg>53</div>
      <div class="post-stats__row"><svg width="20" height="18" viewBox="0 0 20 18"><path d="M10 1l2.5 5.3 5.7.6-4.3 3.9 1.2 5.7L10 13.6 4.9 16.5l1.2-5.7L1.8 6.9l5.7-.6z" fill="none" stroke="#555" stroke-width="1.2"/></svg>122</div>
    </div>
  </div>

  <nav class="footer-menu" aria-label="Main menu">
    <div class="footer-menu__bar footer-menu__bar--left"></div>
    <div class="footer-menu__bar footer-menu__bar--right"></div>

    <!-- Missions -->
    <svg class="footer-menu__icon" style="left:38px" viewBox="0 0 28 28"><path d="M14 2l3.5 7.4 8 .9-6 5.5 1.7 8L14 19.8l-7.2 4 1.7-8-6-5.5 8-.9z" fill="var(--icon)"/></svg>
    <!-- Profile -->
    <svg class="footer-menu__icon" style="left:86px" viewBox="0 0 28 28"><circle cx="14" cy="14" r="12" fill="none" stroke="var(--icon)" stroke-width="2"/><circle cx="14" cy="11" r="4.5" fill="var(--icon)"/><path d="M6 22c1.5-4 4.5-5.5 8-5.5s6.5 1.5 8 5.5a12 12 0 0 1-16 0z" fill="var(--icon)"/></svg>
    <!-- Friends -->
    <svg class="footer-menu__icon" style="left:143px;width:38px;margin-left:-19px" viewBox="0 0 38 28"><g fill="var(--icon)"><circle cx="12" cy="9" r="5"/><path d="M2 24c0-6 4.5-9 10-9s10 3 10 9z"/><circle cx="26" cy="9" r="5"/><path d="M18 24c0-6 2.5-9 8-9s10 3 10 9z"/></g></svg>
    <!-- Home -->
    <svg class="footer-menu__icon" style="left:305px" viewBox="0 0 28 28"><path d="M14 3L2 14h3.5v10h6.5v-7h4v7h6.5V14H26z" fill="var(--icon)"/><rect x="19" y="5" width="3" height="6" fill="var(--icon)"/></svg>
    <!-- Notifications -->
    <svg class="footer-menu__icon" style="left:358px;width:32px;margin-left:-16px" viewBox="0 0 32 28"><g fill="var(--icon)"><path d="M20 4c5.5 0 10 3.3 10 7.5 0 2.3-1.3 4.3-3.4 5.6L28 21l-5-2.4c-1 .2-2 .4-3 .4-5.5 0-10-3.3-10-7.5S14.5 4 20 4z"/><path d="M9 10c-.1.5-.1 1-.1 1.5 0 4.6 4.3 8.3 10 8.8-1.7 2-4.7 3.2-8 3.2-1 0-2-.1-3-.4L3 25l1.5-4C2.9 19.7 2 18 2 16.2 2 13.5 4.9 11 9 10z"/></g></svg>
    <!-- Settings -->
    <svg class="footer-menu__icon" style="left:407px" viewBox="0 0 28 28"><circle cx="14" cy="14" r="7.5" fill="none" stroke="var(--icon)" stroke-width="5"/><circle cx="14" cy="14" r="10.5" fill="none" stroke="var(--icon)" stroke-width="4" stroke-dasharray="4.1 4.1"/></svg>

    <!-- Lumora capture button -->
    <svg class="capture-button" viewBox="0 0 90 90" aria-label="Create a Lumora"><circle cx="45" cy="45" r="40" fill="none" stroke="var(--ink)" stroke-width="6"/><circle cx="45" cy="45" r="40" fill="none" stroke="var(--white)" stroke-width="3"/><circle cx="45" cy="45" r="8" fill="var(--white)"/></svg>
  </nav>
</section>

</body>
</html>
```